DEAN COLLOPY PROPERTY SERVICES

I want a business card that is clean and simple.
'Dean Collopy Property Services' is the title.
Somewhere on the card needs to be 'Carpentry, Tiling, painting and garden services'

On the back of card
PH 087 394 1526
email: deancollopypropertyservices@bluefinchmail.net

I have attached a picture of my other business. I would like the font and design to be similar to the bathroom business.

Many thanks.

```html
<!DOCTYPE html>
<html lang="en">
<head>
<meta charset="utf-8">
<title>Dean Collopy Property Services – Business Card</title>
<link rel="stylesheet" href="https://fonts.googleapis.com/css2?family=Montserrat:wght@400;500&family=Arimo:wght@400&display=swap">
<style>
  :root {
    --ink: #0b0b0b;
    --paper: #ffffff;
    --backdrop: #d9d9d9;
    --ghost: #e4e4e4;
    --text-dark: #1a1a1a;
    --font-brand: "Montserrat", sans-serif;
    --font-contact: "Arimo", sans-serif;
  }
  * { box-sizing: border-box; margin: 0; padding: 0; }
  html, body {
    width: 1200px;
    height: 900px;
    overflow: hidden;
    background: var(--backdrop);
  }
  .sheet {
    position: relative;
    width: 1200px;
    height: 900px;
    display: flex;
    flex-direction: column;
    align-items: center;
    justify-content: center;
    gap: 56px;
  }
  .card {
    position: relative;
    width: 660px;
    height: 380px;
    box-shadow: 0 6px 18px rgba(0, 0, 0, 0.18);
    overflow: hidden;
  }

  /* Front */
  .card-front {
    background: var(--ink);
    display: flex;
    align-items: center;
    justify-content: center;
  }
  .brand {
    font-family: var(--font-brand);
    font-weight: 500;
    color: var(--paper);
    text-align: center;
    line-height: 1;
  }
  .brand-name {
    display: block;
    font-size: 56px;
    letter-spacing: 1px;
  }
  .brand-line {
    display: block;
    margin-top: 12px;
    font-size: 16px;
    letter-spacing: 9px;
    padding-left: 9px;
  }

  /* Back */
  .card-back {
    background: var(--paper);
  }
  .brand-ghost {
    position: absolute;
    top: 44px;
    left: 40px;
    color: var(--ghost);
    text-align: left;
  }
  .brand-ghost .brand-name { font-size: 44px; }
  .brand-ghost .brand-line { font-size: 13px; letter-spacing: 7px; padding-left: 0; margin-top: 10px; }

  .contact-list {
    position: absolute;
    right: 40px;
    top: 170px;
    list-style: none;
    display: flex;
    flex-direction: column;
    align-items: flex-end;
    gap: 22px;
  }
  .contact-item {
    display: flex;
    align-items: center;
    gap: 14px;
    font-family: var(--font-contact);
    font-size: 18px;
    color: var(--text-dark);
  }
  .contact-icon {
    width: 34px;
    height: 40px;
    border-radius: 14px;
    background: var(--ink);
    display: flex;
    align-items: center;
    justify-content: center;
    flex-shrink: 0;
  }
  .services-band {
    position: absolute;
    left: 0;
    right: 0;
    bottom: 30px;
    height: 50px;
    background: var(--ink);
    color: var(--paper);
    font-family: var(--font-brand);
    font-weight: 400;
    font-size: 19px;
    letter-spacing: 2px;
    display: flex;
    align-items: center;
    justify-content: center;
  }
</style>
</head>
<body>
<main class="sheet">

  <section class="card card-front" aria-label="Card front">
    <div class="brand">
      <span class="brand-name">Dean Collopy</span>
      <span class="brand-line">PROPERTY SERVICES</span>
    </div>
  </section>

  <section class="card card-back" aria-label="Card back">
    <div class="brand brand-ghost" aria-hidden="true">
      <span class="brand-name">Dean Collopy</span>
      <span class="brand-line">PROPERTY SERVICES</span>
    </div>

    <ul class="contact-list">
      <li class="contact-item">
        <span class="contact-text">087 394 1526</span>
        <span class="contact-icon">
          <svg width="14" height="22" viewBox="0 0 14 22" aria-hidden="true">
            <rect x="1" y="1" width="12" height="20" rx="2" fill="none" stroke="#fff" stroke-width="1.6"/>
            <line x1="5" y1="17.5" x2="9" y2="17.5" stroke="#fff" stroke-width="1.4"/>
          </svg>
        </span>
      </li>
      <li class="contact-item">
        <span class="contact-text">deancollopypropertyservices@bluefinchmail.net</span>
        <span class="contact-icon">
          <svg width="20" height="14" viewBox="0 0 20 14" aria-hidden="true">
            <rect x="1" y="1" width="18" height="12" fill="none" stroke="#fff" stroke-width="1.6"/>
            <polyline points="1,1 10,8 19,1" fill="none" stroke="#fff" stroke-width="1.6"/>
          </svg>
        </span>
      </li>
    </ul>

    <div class="services-band">CARPENTRY | TILING | PAINTING | GARDEN SERVICES</div>
  </section>

</main>
</body>
</html>
```